Business Card Design Project and Logo Enhancement

This project requires designing a business card for a construction company. It also requires small enhancements on provided logo.
Summary about the company:
Name: Korvellan Group.
Future website. www.korvellan.ca
Korvellan is a home redesign and renovation company providing services in Ottawa Canada area.
It offers the following services:
- Home Additions
- Roofing
- Eavestroughing & Soffit Fascia
- Fencing
- Decks
- Window Installation, and
- Indoor Renovation Including ( Kitchen redesign, Basement finishing, bathroom upgrades, etc)
Logo and Company name background:
Korvellan refers to an ancient empire that was located in Balkans called Veltarians.
Provided logo represents the symbol of Veltarians.
Project Expectation:
Logo:
Attached logo is too SIMPLe. It would be nice adding a bit of design.
That could include different colors or adding a bit of style to the logo.
Business Card
Initial preferred layout/content ( open to other suggestions) :
Preferred type: Vertical with rounded corners
Front side should have:
- Logo
- Company Name
- First Name/ Last name: Ie: Edmir Kollqaj
- Office Phone:
- Direct Phone:
- QR Code linking to www.korvellan.ca, and
- website url. www. korvellan.ca
Back end shall contain:
Professional services offered:
- Large company logo covering most of the card as a water mark
- Divisions Services offered
- Roofing
- Eavestroughing, Soffit, Fascia
- Fencing and Decks
- Indoor Design and Renovation
- Company Phone and
- Company website address: www.korvellan.ca
PSD and other raw files must be provided by the winner.

```html
<!DOCTYPE html>
<html lang="en">
<head>
<meta charset="utf-8">
<title>Korvellan Group – Business Card Back</title>
<link rel="stylesheet" href="https://fonts.googleapis.com/css2?family=Noto+Sans:wght@400&family=Arimo:wght@400&display=swap">
<style>
  :root {
    --page-bg: #ffffff;
    --card-bg: #000000;
    --service-text: #d9d9d9;
    --contact-text: #ffffff;
    --emblem-tone: #574300;
    --emblem-tone-soft: #2b2100;
  }
  html, body {
    margin: 0;
    padding: 0;
    width: 1200px;
    height: 900px;
    overflow: hidden;
    background: var(--page-bg);
  }
  .canvas {
    position: relative;
    width: 1200px;
    height: 900px;
  }
  .card-back {
    position: absolute;
    left: 347px;
    top: 58px;
    width: 506px;
    height: 783px;
    background: var(--card-bg);
    border-radius: 44px;
    overflow: hidden;
  }
  .emblem-watermark {
    position: absolute;
    left: 131px;
    top: 80px;
    width: 244px;
    height: 617px;
    border-radius: 60px;
    background: radial-gradient(ellipse at center, var(--emblem-tone) 0%, var(--emblem-tone-soft) 70%, transparent 100%);
    opacity: 0.45;
  }
  .service-list {
    position: absolute;
    left: 40px;
    top: 104px;
    margin: 0;
    padding: 0;
    list-style: none;
    font-family: "Noto Sans", sans-serif;
    font-size: 26px;
    line-height: 1;
    color: var(--service-text);
  }
  .service-item {
    position: relative;
    height: 89px;
    padding-left: 20px;
    letter-spacing: -0.2px;
  }
  .service-item::before {
    content: "";
    position: absolute;
    left: 2px;
    top: 13px;
    width: 9px;
    height: 9px;
    border-radius: 50%;
    background: var(--contact-text);
  }
  .contact-phone {
    position: absolute;
    left: 82px;
    top: 620px;
    margin: 0;
    font-family: "Arimo", sans-serif;
    font-size: 35px;
    color: var(--contact-text);
  }
  .contact-rule {
    position: absolute;
    left: 84px;
    top: 680px;
    width: 338px;
    height: 2px;
    background: var(--contact-text);
  }
  .contact-web {
    position: absolute;
    left: 82px;
    top: 694px;
    margin: 0;
    font-family: "Arimo", sans-serif;
    font-size: 41px;
    color: var(--contact-text);
  }
</style>
</head>
<body>
  <main class="canvas">
    <section class="card-back" aria-label="Korvellan Group business card, back side">
      <div class="emblem-watermark" role="img" aria-label="Large faint Korvellan emblem watermark"></div>
      <ul class="service-list">
        <li class="service-item">Roofing</li>
        <li class="service-item">Eavestroughing, Soffit, Fascia</li>
        <li class="service-item">Fencing and Decks</li>
        <li class="service-item">Window Installation</li>
        <li class="service-item">Indoor Design and Renovation</li>
      </ul>
      <p class="contact-phone">phone: 000 000 000</p>
      <div class="contact-rule"></div>
      <p class="contact-web">www.korvellan.ca</p>
    </section>
  </main>
</body>
</html>
```